BrightLane Driving School

I need a Facebook page for my Driving School. I teach mostly teenagers how to drive in New Hampshire but also do private classes for adults as well. More info can be found at brightlanelessons.com

```html
<!DOCTYPE html>
<html lang="en">
<head>
<meta charset="utf-8">
<title>BrightLane Driving School – Facebook Cover</title>
<link rel="stylesheet" href="https://fonts.googleapis.com/css2?family=Poppins:wght@400;600;700;800&display=swap">
<style>
  :root {
    --yellow: #f2c10f;
    --ink: #111111;
    --bar: #262626;
    --page: #e4e4e4;
    --white: #ffffff;
    --tag-edge: #9a9a9a;
  }
  * { margin: 0; padding: 0; box-sizing: border-box; }
  html, body { width: 1200px; height: 854px; overflow: hidden; background: var(--page); }
  body { font-family: "Poppins", sans-serif; }

  .cover {
    position: absolute; left: 34px; top: 131px;
    width: 1132px; height: 592px; overflow: hidden;
  }
  .cover-art { position: absolute; inset: 0; }

  .brand {
    position: absolute; left: 66px; top: 62px;
    display: flex; align-items: center; gap: 12px;
  }
  .brand-dot { width: 22px; height: 22px; border-radius: 50%; background: var(--yellow); }
  .brand-name { font-weight: 800; font-size: 27px; color: var(--ink); line-height: 1; }
  .brand-phone {
    position: absolute; left: 100px; top: 100px;
    font-weight: 800; font-size: 15px; color: var(--ink); letter-spacing: 1px;
  }

  .headline {
    position: absolute; left: 58px; top: 190px;
    font-weight: 800; font-size: 53px; line-height: 1.08; color: var(--ink);
    letter-spacing: -0.5px;
  }
  .tagline {
    position: absolute; left: 58px; top: 309px;
    font-size: 16.5px; color: #222; font-weight: 400;
  }
  .tagline strong { font-weight: 700; }

  .services { position: absolute; left: 60px; top: 370px; display: flex; gap: 4px; }
  .service {
    position: relative; width: 184px; height: 62px;
    display: flex; align-items: center; justify-content: center; text-align: center;
    font-weight: 700; font-size: 15.5px; line-height: 1.4; color: var(--ink);
  }
  .service::before, .service::after {
    content: ""; position: absolute; inset: 0; transform: skewX(-14deg);
  }
  .service::before { border: 1px solid var(--tag-edge); left: -10px; top: -6px; right: 8px; bottom: 4px; }
  .service::after { background: var(--yellow); }
  .service span { position: relative; z-index: 1; }

  .contact-bar {
    position: absolute; left: 0; top: 468px; height: 46px; width: 648px;
    background: var(--bar);
    clip-path: polygon(0 0, 632px 0, 648px 100%, 0 100%);
    display: flex; align-items: center; padding-left: 60px; gap: 10px;
    font-size: 21px; color: var(--white);
  }
  .contact-bar .phone { color: var(--yellow); font-weight: 700; }
  .contact-bar .divider { margin: 0 6px; }
  .contact-bar .web strong { color: var(--yellow); font-weight: 700; }
  .contact-bar svg { width: 22px; height: 22px; }
</style>
</head>
<body>
<main class="cover">
  <svg class="cover-art" width="1132" height="592" viewBox="0 0 1132 592">
    <defs>
      <linearGradient id="scene" x1="0" y1="0" x2="0" y2="1">
        <stop offset="0" stop-color="#cfe0f2"/>
        <stop offset="0.45" stop-color="#eef1f4"/>
        <stop offset="0.62" stop-color="#b9c0c6"/>
        <stop offset="0.7" stop-color="#6f7377"/>
        <stop offset="1" stop-color="#8a8b8c"/>
      </linearGradient>
      <linearGradient id="lesson" x1="0" y1="0" x2="1" y2="1">
        <stop offset="0" stop-color="#c9ccd0"/>
        <stop offset="0.4" stop-color="#7d8a6a"/>
        <stop offset="0.7" stop-color="#4d86c9"/>
        <stop offset="1" stop-color="#c7cacd"/>
      </linearGradient>
    </defs>
    <rect width="1132" height="592" fill="url(#scene)" role="img" aria-label="City skyline beyond an open road with lane markings"/>
    <polygon points="555,0 1132,0 1132,514 750,514" fill="url(#lesson)" role="img" aria-label="Smiling student driver holding up her new licence while an instructor takes notes in the passenger seat"/>
    <polygon points="518,0 555,0 648,252 605,252" fill="var(--yellow)"/>
    <polygon points="1040,0 1132,0 1132,210" fill="var(--yellow)"/>
  </svg>

  <div class="brand">
    <span class="brand-dot"></span>
    <span class="brand-name">BrightLane Driving School</span>
  </div>
  <div class="brand-phone">603 555 0147</div>

  <h1 class="headline">AWARD-WINNING<br>DRIVING SCHOOL</h1>
  <p class="tagline">BrightLane Driving School in <strong>western New Hampshire</strong></p>

  <ul class="services" style="list-style:none">
    <li class="service"><span>Teenage Group<br>Driver Education</span></li>
    <li class="service"><span>Individual Driver<br>Education</span></li>
    <li class="service"><span>Senior Driver<br>Evaluations</span></li>
  </ul>

  <div class="contact-bar">
    <svg viewBox="0 0 24 24" aria-hidden="true"><circle cx="12" cy="12" r="11" fill="var(--yellow)"/><path d="M8.5 6.5l2 2-1.2 1.6c.7 1.6 2 2.9 3.6 3.6l1.6-1.2 2 2-1.3 1.8c-4-.5-7.4-3.9-7.9-7.9z" fill="var(--bar)"/></svg>
    <span class="phone">603-555-0147</span>
    <span class="divider">|</span>
    <svg viewBox="0 0 24 24" aria-hidden="true"><circle cx="12" cy="12" r="11" fill="var(--yellow)"/><g fill="none" stroke="var(--bar)" stroke-width="1.4"><circle cx="12" cy="12" r="6.5"/><ellipse cx="12" cy="12" rx="3" ry="6.5"/><path d="M5.5 12h13"/></g></svg>
    <span class="web">www.<strong>brightlanelessons</strong>.com</span>
  </div>
</main>
</body>
</html>
```